Vantor Health Group Presentation Folder, for Cancer Awareness, VERY COLORFUL AND MODERN

Presentation Folder I know pretty much what i want so it should be very eazy , I have included files from folders I use now rebrand them to my new company they will be fine, no sense re creating the wheel
Full Bleed Size
20.87" x 16.68"
53 x 42.4 cm
6260 x 5004 pixels
Document Trim Size
20.75" x 16.56"
52.7 x 42.1 cm
6225 x 4969 pixels
Updates

Low design quality

Industry/Entity Type

Medical

Font styles to use
Serif

Colors

Designer to choose colors to be used in the design.

Requirements
Must have
• really I am not looking for some one to redesign, we like our folder front page and would like to see new word information added., there are two folder front pages to choose from
• So Keep the original front page and redesign the back page and the pockets
• Can Make your Design off of one of the ones I already uploaded
Nice to have
• Keep the same color schemes, Keep the original front page and redesign the back page and the pockets
Should not have
• DO not recreate the front covers, use what I gave you and just rebrand

```html
<!DOCTYPE html>
<html lang="en">
<head>
<meta charset="utf-8">
<title>Vantor Health Group – Presentation Folder</title>
<link rel="stylesheet" href="https://fonts.googleapis.com/css2?family=Raleway:wght@400;500;600;700&display=swap">
<style>
  :root{
    --backdrop:#3a3a3a;
    --paper:#ffffff;
    --pocket-edge:#d4d4d6;
    --navy:#0f1f5c;
    --blue-text:#243a8f;
    --pink:#ec6f8d;
    --sky:#4fc3e8;
    --body-grey:#555a63;
    --slate:#4f5ea8;
  }
  *{box-sizing:border-box;margin:0;padding:0}
  html,body{width:902px;height:1200px;overflow:hidden;background:var(--backdrop)}
  body{font-family:"Raleway",Arial,sans-serif}
  .canvas{position:relative;width:902px;height:1200px;overflow:hidden}
  .folder-shape{position:absolute;left:0;top:0}
  .abs{position:absolute}

  .family-photo{left:100px;top:292px;width:274px;height:274px;border-radius:50%;
    background:radial-gradient(circle at 50% 42%,#f1e2d3 0%,#d8b59a 45%,#a9806c 72%,#26306a 100%)}
  .intro-copy{left:63px;top:579px;width:343px;font-size:10px;line-height:13.2px;color:var(--body-grey);text-align:justify}
  .intro-copy strong{color:var(--pink);font-weight:700}
  .tagline{left:40px;top:670px;width:360px;text-align:center;font-weight:700}
  .tagline .lead{color:var(--pink);font-size:13.5px;line-height:18px}
  .tagline .rest{color:var(--slate);font-size:13.5px;line-height:17.5px}

  .headline{left:455px;top:306px;width:390px;text-align:center}
  .headline h1{color:var(--pink);font-size:22px;font-weight:600;letter-spacing:.3px}
  .headline h2{color:var(--blue-text);font-size:10.6px;font-weight:700;margin-top:5px;letter-spacing:.2px}
  .headline p{color:var(--sky);font-size:9.4px;line-height:12px;margin-top:11px;text-transform:uppercase;letter-spacing:.2px}

  .meal-photo{left:483px;top:447px;width:328px;height:230px;transform:rotate(3deg);
    border:4px solid var(--paper);box-shadow:2px 4px 8px rgba(0,0,0,.35);
    background:linear-gradient(160deg,#eef0f2 0%,#d8cfc2 40%,#a88e74 70%,#7d7468 100%)}
  .ribbon{left:764px;top:413px;width:36px;height:62px;border-radius:18px 18px 4px 4px;
    background:linear-gradient(90deg,#6fc6e8 0%,#b79bd1 50%,#e98fb6 100%);transform:rotate(-12deg)}

  .test-line{left:470px;top:718px;display:flex;align-items:center;gap:12px}
  .test-line .dot{width:34px;height:34px;border-radius:50%;background:var(--navy)}
  .test-line span{color:var(--blue-text);font-size:14px;font-weight:500;letter-spacing:.2px}

  .pocket-imprint{left:108px;top:781px;width:240px;text-align:center;transform:rotate(180deg)}
  .pocket-imprint .name{color:var(--pink);font-size:15px;font-weight:500;letter-spacing:.8px}
  .pocket-imprint .sub{color:var(--slate);font-size:10.5px;margin-top:2px}

  .pocket-brand{left:560px;top:830px;display:flex;align-items:center;gap:10px;transform:rotate(180deg)}
  .pocket-brand .mark{width:56px;height:56px;border-radius:50%;background:var(--navy)}
  .pocket-brand .word{color:var(--navy);font-size:19px;font-weight:700;line-height:19px;letter-spacing:.5px;border-left:2px solid var(--navy);padding-left:8px}
</style>
</head>
<body>
<main class="canvas">
  <svg class="folder-shape" width="902" height="1200" viewBox="0 0 902 1200" aria-hidden="true">
    <path fill="var(--paper)" d="M34 262 H852 V963 H485 C470 963 462 940 458 900 C454 840 452 800 448 771 H441 C438 800 432 860 420 920 C414 950 405 963 393 963 H34 Z"/>
    <line x1="34" y1="771" x2="852" y2="771" stroke="#eeeeee" stroke-width="1"/>
    <rect x="34" y="771" width="31" height="192" fill="var(--pocket-edge)"/>
    <rect x="822" y="771" width="30" height="192" fill="var(--pocket-edge)"/>
    <g stroke="#b9b9b9" stroke-width="1.2">
      <line x1="165" y1="840" x2="188" y2="817"/>
      <line x1="293" y1="817" x2="316" y2="840"/>
      <line x1="165" y1="880" x2="188" y2="903"/>
      <line x1="293" y1="903" x2="316" y2="880"/>
    </g>
  </svg>

  <div class="abs family-photo" role="img" aria-label="Photo of a smiling three-generation family held in a navy hand-shaped frame"></div>

  <p class="abs intro-copy"><strong>Hereditary cancer screening</strong> provides vital information to help people with a strong personal or family history of cancer understand their own risk of developing the disease. With this information, they can take steps to Potentially Prevent Cancer, Delay the Onset of Cancer or Catch it at an Earlier stage when outcomes and survival rates are Better.</p>

  <div class="abs tagline">
    <div class="lead">Don't be Afraid of the Answer:</div>
    <div class="rest">Knowledge is Power and Power Eradicates Fear.<br>When You are Fearless, You Will Make all the<br>Right Choices!</div>
  </div>

  <header class="abs headline">
    <h1>HEREDITARY CANCER SCREENING</h1>
    <h2>DOCTORS ARE THE GATEKEEPERS TO GENETIC TESTING.</h2>
    <p>We have an obligation to help patients understand genetic<br>risk and how testing can guide heath care decisions.</p>
  </header>

  <div class="abs meal-photo" role="img" aria-label="Photo of a family sharing a meal at an outdoor table"></div>
  <div class="abs ribbon" role="img" aria-label="Pink and blue cancer awareness ribbon"></div>

  <div class="abs test-line">
    <div class="dot"></div>
    <span>THE TEST YOU ORDER FOR YOUR PATIENTS</span>
  </div>

  <div class="abs pocket-imprint">
    <div class="name">VANTOR HEALTH GROUP</div>
    <div class="sub">a division of Meridian Medical Sales LLC</div>
  </div>

  <div class="abs pocket-brand">
    <div class="mark"></div>
    <div class="word">VANTOR<br>HEALTH<br>GROUP</div>
  </div>
</main>
</body>
</html>
```